PLIMOR

Require a design to fit on an A5 page, this is a page within a booklet by others hence it needs to be portable to that end user.
I have attached a picture of a banner we have used in the past as a basis for the design.
As this is for a conference on vegetable growing it needs to have that theme within the design together with the attached logo and a web/ email address and phone number.
Our products dispense fertiliser into irrigation water which is termed fertigation
www.quorvitdosingunits.com.au for further reference.

Reason: some designers that indicated they had accepted the project late need some more time

```html
<!DOCTYPE html>
<html lang="en">
<head>
<meta charset="utf-8">
<title>Quorvit – Change the way you think about fertilising</title>
<link rel="stylesheet" href="https://fonts.googleapis.com/css2?family=Marcellus&family=Roboto+Slab:wght@400;600&display=swap">
<style>
  :root {
    --sky-top: #3fb3e6;
    --sky-mid: #8fd3f2;
    --haze: #e6f3fa;
    --sand: #f4ece9;
    --navy: #1d2f6b;
    --leaf-green: #2f8a2a;
    --band-green: #8cc63f;
    --white: #ffffff;
    --logo-ink: #1a1a1a;
    --logo-gold: #c9a94a;
  }
  * { margin: 0; padding: 0; box-sizing: border-box; }
  html, body { width: 845px; height: 1200px; overflow: hidden; background: var(--white); }

  .page {
    position: absolute;
    left: 0; top: 0;
    width: 1200px; height: 845px;
    transform-origin: 0 0;
    transform: translate(0, 1200px) rotate(-90deg);
    overflow: hidden;
    background: linear-gradient(180deg, var(--sky-top) 0%, var(--sky-mid) 35%, var(--haze) 65%, var(--sand) 100%);
    font-family: "Marcellus", serif;
  }

  .brand {
    position: absolute;
    right: 50px; top: 62px;
    display: flex; align-items: center; gap: 18px;
  }
  .brand-mark { width: 86px; height: 86px; background: var(--logo-gold); }
  .brand-name {
    font-family: "Marcellus", serif;
    font-size: 84px; line-height: 1;
    color: var(--logo-ink);
    letter-spacing: 4px;
  }

  .headline {
    position: absolute;
    left: 82px; top: 84px;
    color: var(--navy);
    text-transform: uppercase;
    line-height: 1;
  }
  .headline .line-1 { font-size: 50px; font-weight: 700; letter-spacing: 1px; display: block; }
  .headline .line-2 { font-size: 32px; display: block; margin-top: 8px; }
  .headline .line-3 { font-size: 44px; display: block; margin-top: 6px; }
  .headline .accent { font-size: 78px; color: var(--leaf-green); letter-spacing: 2px; }

  .rule {
    position: absolute;
    left: 0; right: 0; top: 252px;
    height: 2px;
    background: var(--leaf-green);
    opacity: .7;
  }

  .produce {
    position: absolute;
    left: 290px; top: 290px;
    width: 870px; height: 480px;
    border-radius: 240px 240px 40px 40px;
    background: radial-gradient(ellipse at 60% 40%, #5fb33a 0%, #3f8f2a 35%, #c23a2a 60%, rgba(160,120,70,.6) 80%, rgba(255,255,255,0) 100%);
  }

  .contact-band {
    position: absolute;
    left: 0; right: 0; bottom: 0;
    height: 72px;
    background: var(--band-green);
    display: flex; align-items: center; justify-content: space-between;
    padding: 0 40px;
    font-family: "Roboto Slab", serif;
    font-size: 19px;
    color: var(--white);
  }
  .contact-band .divider { width: 2px; height: 34px; background: var(--white); opacity: .8; }
</style>
</head>
<body>
  <main class="page">
    <header class="brand">
      <span class="brand-name">QUORVIT</span>
      <span class="brand-mark" aria-hidden="true"></span>
    </header>

    <h1 class="headline">
      <span class="line-1">Change</span>
      <span class="line-2">The way you think</span>
      <span class="line-3">About <span class="accent">Fertilising</span></span>
    </h1>

    <div class="rule" aria-hidden="true"></div>

    <div class="produce" role="img" aria-label="Wicker basket of fresh vegetables – capsicums, lettuce, eggplant, onions, cauliflower – beneath a large dewy green leaf"></div>

    <footer class="contact-band">
      <span class="contact email">Email: info@quorvitfertilising.com.au</span>
      <span class="divider" aria-hidden="true"></span>
      <span class="contact phone">Mobile: +61 7 4000 0000</span>
      <span class="divider" aria-hidden="true"></span>
      <span class="contact web">Website: quorvitdosingunits.com.au</span>
    </footer>
  </main>
</body>
</html>
```